Building Maintenance Company Capability Statement

We would like a capability statement designed please.

Let us know where we can supply the written text.

Ideally, most of the information will be on our website.
www.tidewellgroup.com.au

Target Market(s)

Strata and building managers. schools and educational facilities, retirement and aged care.

Industry/Entity Type

Building

Font styles to use
Other font styles liked:
• nanito sans light

Requirements
Must have
• Images of people working (we can supply)
Easy to skim read
Colourful and attractive
Should not have
• lots of words

```html
<!DOCTYPE html>
<html lang="en">
<head>
<meta charset="utf-8">
<title>Tidewell Group – Capability Statement</title>
<link href="https://fonts.googleapis.com/css2?family=Roboto+Condensed:wght@300;400;700&family=Open+Sans:wght@400;600&display=swap" rel="stylesheet">
<style>
:root{
  --navy:#123f73;
  --red:#d71f30;
  --red-dark:#a5141f;
  --sky:#1b86cf;
  --ink:#222;
  --panel:#ececec;
  --backdrop:#2e2e2e;
  --white:#fff;
}
*{margin:0;padding:0;box-sizing:border-box}
html,body{width:900px;height:1200px;overflow:hidden;background:var(--backdrop)}
.flyer{position:absolute;left:110px;top:90px;width:692px;height:980px;background:var(--white);overflow:hidden;font-family:"Open Sans",Arial,sans-serif;color:var(--ink)}
.abs{position:absolute}
.brand{left:0;right:0;top:34px;display:flex;justify-content:center;align-items:center;gap:14px}
.brand-dot{width:46px;height:46px;border-radius:50%;background:var(--navy)}
.brand-name{font-family:"Roboto Condensed",Arial,sans-serif;font-weight:700;font-size:36px;color:var(--navy);letter-spacing:.5px}
.rule{left:0;top:116px;width:692px;height:14px;background:var(--sky)}
.hero-photo{left:300px;top:130px;width:392px;height:342px;background:linear-gradient(90deg,rgba(255,255,255,1) 0%,rgba(214,218,222,.85) 25%,#b9bec4 60%,#9ea6ad 100%)}
.headline{left:30px;width:310px;top:212px;text-align:center;font-family:"Roboto Condensed",Arial,sans-serif;color:var(--navy);line-height:1}
.headline .lead{font-size:13px;letter-spacing:.3px;margin-bottom:10px}
.headline .l1{font-size:34px;font-weight:700}
.headline .l2{font-size:50px;font-weight:700;color:var(--red);margin-top:4px}
.headline .l3{font-size:45px;font-weight:300;margin-top:4px}
.bands{left:0;top:440px}
.section-title{font-family:"Roboto Condensed",Arial,sans-serif;font-weight:700;color:var(--white);font-size:32px}
.about-title{left:40px;top:447px}
.phone-num{left:398px;top:514px;font-family:"Roboto Condensed",Arial,sans-serif;font-weight:700;font-size:44px;color:var(--white);letter-spacing:1px}
.about-text{left:30px;top:515px;width:290px;font-size:10.6px;line-height:14.4px;text-align:justify}
.why{left:360px;width:332px;top:614px;text-align:center;font-family:"Roboto Condensed",Arial,sans-serif;font-weight:700;font-size:22px;color:var(--navy)}
.why span{color:var(--red)}
.checks{left:380px;top:646px;width:312px;height:74px;background:var(--panel);display:flex}
.check{flex:1;display:flex;flex-direction:column;align-items:center;justify-content:flex-end;padding-bottom:6px;font-size:11px;border-right:2px solid #d3d3d3}
.check:last-child{border-right:none}
.check svg{margin-bottom:8px}
.service-title{left:30px;top:692px}
.services{left:0;top:748px;font-size:11px;line-height:13px}
.service{position:absolute;display:flex;align-items:center;gap:14px;width:180px}
.icon{width:30px;height:30px;flex:none;display:flex;align-items:center;justify-content:center}
.icon.red{background:var(--red)}
.icon.navy{background:var(--navy)}
.work-photo{left:350px;top:746px;width:342px;height:234px;background:linear-gradient(160deg,#c9c2b5 0%,#a0654a 55%,#7a3f2a 100%);clip-path:polygon(30px 0,100% 0,100% 100%,0 100%)}
.footer-url{left:86px;top:955px;font-size:12px;letter-spacing:3.2px;color:var(--white);font-weight:600}
</style>
</head>
<body>
<main class="flyer">
  <header class="abs brand">
    <div class="brand-dot"></div>
    <div class="brand-name">TIDEWELL GROUP</div>
  </header>
  <div class="abs rule"></div>

  <div class="abs hero-photo" role="img" aria-label="Tradesman in hi-vis shirt standing on a stepladder inside a building under repair"></div>

  <div class="abs headline">
    <div class="lead">WE PROVIDE COST EFFECTIVE SOLUTIONS TO</div>
    <div class="l1">YOUR BUILDING AND</div>
    <div class="l2">MAINTENANCE</div>
    <div class="l3">REQUIREMENTS</div>
  </div>

  <svg class="abs bands" width="692" height="300" viewBox="0 0 692 300">
    <polygon points="0,6 440,6 430,40 0,40" fill="var(--red)"/>
    <polygon points="0,2 212,2 196,46 0,46" fill="var(--navy)"/>
    <polygon points="430,6 692,6 692,38 438,38" fill="var(--red)"/>
    <polygon points="352,38 440,18 440,58 352,58" fill="var(--red-dark)"/>
    <rect x="352" y="57" width="340" height="86" fill="var(--red)"/>
    <rect x="332" y="78" width="48" height="48" fill="var(--navy)"/>
    <path d="M346 92c2-2 5-2 6 0l3 4c1 2 0 3-1 4l-2 1c1 3 5 7 8 8l1-2c1-1 3-2 4-1l4 3c2 1 2 4 0 6-2 2-5 3-8 1-7-3-13-9-16-16-1-3 0-6 1-8z" fill="var(--white)"/>
  </svg>
  <div class="abs section-title about-title">ABOUT US</div>
  <div class="abs phone-num">0400 318 742</div>

  <p class="abs about-text">We provide high quality maintenance and building solutions to our customers whilst improving the lives of the people who we work with, and partner with.<br>We specialise in small-to-medium commercial building maintenance contracting and strive to offer quick response to the challenges our clients face.<br>We aim to deliver quality and value wherever possible with a solutions-focused approach. This focus on quick turnaround times without sacrificing quality lays a solid foundation for long-term relationships with our clients.</p>

  <div class="abs why">WHY CHOOSE <span>TIDEWELL</span></div>
  <div class="abs checks">
    <div class="check"><svg width="38" height="32" viewBox="0 0 38 32"><path d="M2 17l10 12L36 2" fill="none" stroke="var(--red)" stroke-width="5"/></svg>Experienced</div>
    <div class="check"><svg width="38" height="32" viewBox="0 0 38 32"><path d="M2 17l10 12L36 2" fill="none" stroke="var(--red)" stroke-width="5"/></svg>Trusted</div>
    <div class="check"><svg width="38" height="32" viewBox="0 0 38 32"><path d="M2 17l10 12L36 2" fill="none" stroke="var(--red)" stroke-width="5"/></svg>Reliable</div>
    <div class="check"><svg width="38" height="32" viewBox="0 0 38 32"><path d="M2 17l10 12L36 2" fill="none" stroke="var(--red)" stroke-width="5"/></svg>Willing</div>
  </div>

  <svg class="abs" style="left:0;top:686px" width="270" height="46" viewBox="0 0 270 46">
    <polygon points="0,0 268,0 246,46 0,46" fill="var(--red)"/>
  </svg>
  <div class="abs section-title service-title">OUR <span style="color:var(--white)">SERVICE</span></div>

  <div class="abs services">
    <div class="service" style="left:0;top:0"><div class="icon red"><svg width="16" height="16"><rect x="2" y="2" width="12" height="12" fill="none" stroke="#fff" stroke-width="1.5"/></svg></div>plastering</div>
    <div class="service" style="left:0;top:38px"><div class="icon navy"><svg width="16" height="16"><path d="M2 14L14 2M2 2l12 12" stroke="#fff" stroke-width="2"/></svg></div>carpentry and repairs</div>
    <div class="service" style="left:0;top:76px"><div class="icon red"><svg width="18" height="12"><rect x="1" y="1" width="16" height="7" fill="none" stroke="#fff" stroke-width="1.5"/><path d="M4 11h10" stroke="#fff"/></svg></div>ac installations</div>
    <div class="service" style="left:0;top:112px"><div class="icon navy"><svg width="18" height="14"><path d="M1 12c4-4 12-4 16 0M9 12V3" stroke="#fff" stroke-width="1.5" fill="none"/></svg></div>landscaping</div>
    <div class="service" style="left:0;top:150px"><div class="icon red"><svg width="16" height="16"><path d="M2 4h10v6M12 12v2" stroke="#fff" stroke-width="2" fill="none"/></svg></div>plumbing</div>
    <div class="service" style="left:166px;top:-4px"><div class="icon red"><svg width="18" height="16"><path d="M1 8L9 1l8 7M4 7v8h10V7" stroke="#fff" stroke-width="1.5" fill="none"/></svg></div>building refurbishment<br>and upgrade works</div>
    <div class="service" style="left:166px;top:46px"><div class="icon navy"><svg width="16" height="16"><rect x="1" y="2" width="12" height="5" fill="#fff"/><path d="M8 7v8" stroke="#fff" stroke-width="2"/></svg></div>internal and external<br>painting works</div>
    <div class="service" style="left:166px;top:94px"><div class="icon red"><svg width="16" height="16"><path d="M5 1v5M11 1v5M3 6h10v3a5 5 0 0 1-10 0z" stroke="#fff" stroke-width="1.5" fill="none"/></svg></div>electrical</div>
    <div class="service" style="left:166px;top:138px"><div class="icon navy"><svg width="18" height="14"><path d="M1 12L9 3l8 9" stroke="#fff" stroke-width="2" fill="none"/></svg></div>roofing</div>
  </div>

  <div class="abs work-photo" role="img" aria-label="Worker in hi-vis shirt and hat kneeling while laying timber decking"></div>

  <svg class="abs" style="left:0;top:950px" width="480" height="30" viewBox="0 0 480 30">
    <polygon points="0,0 476,0 466,30 0,30" fill="var(--navy)"/>
  </svg>
  <div class="abs footer-url">www.tidewellgroup.com.au</div>
</main>
</body>
</html>
```